Flyer for Beacon Ledger & Returns, a local tax practice

Flyer for my business to be distributed locally in the Western Suburb of Melbourne (Size: DL, Fold: Flat, Backside: Blank) This will include below information (Font, color and capitalization of the text is for the designer's creativity):
Beacon Ledger & Returns Your Local Tax Accountant
ABN: 71 284 519 036
Address: 9 Mirra Close, Tarwin Heights
dovpelk@blrau.com.au
Call Florin on 0417 865 209 to book your appointment
Services we offer:
Individual & Company Tax Returns
Company & Trust formation
Business Advisory
Bookkeeping
BAS & IAS
Payroll
TPAR
Please include the logo of the business attached which was designed by ArtHarbor few years ago.
Please include the QNE, WRD and Pulva logos somewhere in the bottom, preferable the same size and aligned (attached)

```html
<!DOCTYPE html>
<html lang="en">
<head>
<meta charset="utf-8">
<title>Beacon Ledger &amp; Returns – Flyer</title>
<link rel="stylesheet" href="https://fonts.googleapis.com/css2?family=Montserrat:wght@600;700;800&display=swap">
<style>
  :root {
    --charcoal: #4f4f4f;
    --orange: #e2773e;
    --ink: #4a4a4a;
    --white: #ffffff;
    --navy: #2c2f7a;
    --plus: #a9aec2;
    --badge-sky: #13b5ea;
    --badge-teal: #1287b0;
    --badge-lime: #b2d62a;
  }
  * { margin: 0; padding: 0; box-sizing: border-box; }
  html, body { width: 1200px; height: 848px; overflow: hidden; background: var(--white); }
  .flyer {
    position: relative; width: 1200px; height: 848px; overflow: hidden;
    background: var(--white);
    font-family: "Montserrat", sans-serif;
  }
  .block { position: absolute; }
  .block--hero { left: 0; top: 0; width: 484px; height: 571px; background: var(--charcoal); }
  .block--tab-top { left: 85px; top: 0; width: 75px; height: 131px; background: var(--orange); }
  .block--contact { left: 85px; top: 499px; width: 544px; height: 264px; background: var(--orange); }
  .block--contact-side { left: 629px; top: 499px; width: 143px; height: 264px; background: var(--charcoal); }
  .block--edge { left: 1170px; top: 499px; width: 30px; height: 264px; background: var(--orange); }
  .block--tab-bottom { left: 85px; top: 818px; width: 75px; height: 30px; background: var(--charcoal); }

  .headline {
    position: absolute; left: 78px; top: 156px;
    color: var(--white); font-weight: 800; font-size: 49px; line-height: 50.5px;
    text-transform: uppercase; letter-spacing: 0.5px;
  }

  .brand {
    position: absolute; left: 510px; top: 33px;
    display: flex; align-items: center; gap: 14px;
  }
  .brand__mark { width: 48px; height: 48px; background: var(--charcoal); flex: none; }
  .brand__name { color: var(--orange); font-weight: 700; font-size: 24px; letter-spacing: 0.2px; white-space: nowrap; }

  .decor { position: absolute; }
  .decor--plus-top { left: 914px; top: 0; }
  .decor--rings { left: 1102px; top: 10px; }
  .decor--plus-bottom { left: 866px; top: 795px; }

  .services { position: absolute; left: 547px; top: 150px; }
  .services__title {
    font-weight: 800; font-size: 27px; line-height: 30px; color: var(--ink);
    text-transform: uppercase;
  }
  .services__title span { color: var(--orange); }
  .services__rule { width: 82px; height: 3px; background: var(--orange); margin-top: 14px; }
  .services__list { list-style: none; margin-top: 16px; }
  .services__list li {
    position: relative; padding-left: 22px;
    font-weight: 700; font-size: 23px; line-height: 33px; color: var(--ink);
  }
  .services__list li::before {
    content: ""; position: absolute; left: 3px; top: 14px;
    width: 6px; height: 6px; border-radius: 50%; background: var(--ink);
  }

  .contact {
    position: absolute; left: 131px; top: 560px; font-style: normal;
    color: var(--white); font-weight: 700; font-size: 27px; line-height: 36.5px;
  }

  .call {
    position: absolute; left: 141px; top: 779px;
    color: var(--ink); font-weight: 700; font-size: 20px;
  }

  .badges { position: absolute; left: 790px; top: 505px; }
  .badge-caption {
    position: absolute; left: 1041px; top: 616px; width: 100px;
    text-align: center; color: #333; font-weight: 600; font-size: 9.5px; line-height: 14px;
  }
</style>
</head>
<body>
<main class="flyer">
  <div class="block block--hero"></div>
  <div class="block block--tab-top"></div>
  <div class="block block--contact"></div>
  <div class="block block--contact-side"></div>
  <div class="block block--edge"></div>
  <div class="block block--tab-bottom"></div>

  <h1 class="headline">Beacon<br>Ledger &amp;<br>Returns<br>Your Local<br>Tax<br>Accountant</h1>

  <div class="brand">
    <span class="brand__mark"></span>
    <span class="brand__name">Beacon Ledger &amp; Returns</span>
  </div>

  <svg class="decor decor--plus-top" width="90" height="82" viewBox="0 0 90 82" aria-hidden="true">
    <g stroke="var(--plus)" stroke-width="1.5">
      <path d="M7 2v10M2 7h10M31.5 2v10M26.5 7h10M56 2v10M51 7h10M80.5 2v10M75.5 7h10
               M7 25v10M2 30h10M31.5 25v10M26.5 30h10M56 25v10M51 30h10M80.5 25v10M75.5 30h10
               M7 48v10M2 53h10M31.5 48v10M26.5 53h10M56 48v10M51 53h10M80.5 48v10M75.5 53h10
               M7 70v10M2 75h10M31.5 70v10M26.5 75h10M56 70v10M51 75h10M80.5 70v10M75.5 75h10"/>
    </g>
  </svg>

  <svg class="decor decor--rings" width="24" height="80" viewBox="0 0 24 80" aria-hidden="true">
    <g fill="none" stroke="var(--navy)" stroke-width="1.6">
      <circle cx="10" cy="11" r="6.5"/><circle cx="10" cy="39" r="6.5"/><circle cx="10" cy="67" r="6.5"/>
    </g>
  </svg>

  <svg class="decor decor--plus-bottom" width="90" height="53" viewBox="0 0 90 53" aria-hidden="true">
    <g stroke="var(--plus)" stroke-width="1.5">
      <path d="M8 3v10M3 8h10M32.5 3v10M27.5 8h10M57 3v10M52 8h10M81.5 3v10M76.5 8h10
               M8 26v10M3 31h10M32.5 26v10M27.5 31h10M57 26v10M52 31h10M81.5 26v10M76.5 31h10
               M8 49v10M32.5 49v10M57 49v10M81.5 49v10"/>
    </g>
  </svg>

  <section class="services">
    <h2 class="services__title">Services We<br><span>Offer</span></h2>
    <div class="services__rule"></div>
    <ul class="services__list">
      <li>Individual &amp; Company Tax Returns</li>
      <li>Company &amp; Trust Formation</li>
      <li>Business Advisory</li>
      <li>Bookkeeping</li>
      <li>BAS &amp; IAS</li>
      <li>Payroll</li>
      <li>TPAR</li>
    </ul>
  </section>

  <address class="contact">
    ABN: 71 284 519 036<br>
    Address: 9 Mirra Close, Tarwin<br>Heights<br>
    dovpelk@blrau.com.au
  </address>

  <p class="call">Call Florin on 0417 865 209 to book your appointment</p>

  <svg class="badges" width="380" height="270" viewBox="790 505 380 270" role="img" aria-label="Partner, registration and membership badges">
    <defs>
      <linearGradient id="memberTone" x1="0" y1="0" x2="1" y2="1">
        <stop offset="0" stop-color="#c0338a"/>
        <stop offset="0.5" stop-color="#2c2f7a"/>
        <stop offset="1" stop-color="#5cc6ea"/>
      </linearGradient>
    </defs>
    <circle cx="851" cy="564" r="51" fill="var(--badge-sky)"/>
    <circle cx="959" cy="564" r="51" fill="var(--badge-teal)"/>
    <circle cx="1091" cy="561" r="49" fill="var(--badge-lime)"/>
    <circle cx="945" cy="705" r="44" fill="url(#memberTone)"/>
  </svg>

  <p class="badge-caption">Tax Agent<br>38172605</p>
</main>
</body>
</html>
```